Velvet Dare Age Verification Landing Page

To create a visually appealing design for the landing page of the adult game "Velvet Dare" that confirms the visitor's age.
The design should have a simple and visually appealing look that focuses on two buttons labeled "Yes" and "No". The purpose of the page is to confirm that the visitor is 18 years of age or older before accessing the game's content. Responsive design that works well on desktop and mobile devices. The final output should be delivered in PSD, AI, or Sketch format, along with any necessary images or assets.
I have also attached examples.

```html
<!DOCTYPE html>
<html lang="en">
<head>
<meta charset="utf-8">
<title>Velvet Dare – Age Verification</title>
<link rel="stylesheet" href="https://fonts.googleapis.com/css2?family=Fondamento&family=Roboto:wght@400;500;700&display=swap">
<style>
:root{
  --page:#050409;
  --frame:#2a1a55;
  --ink:#ffffff;
  --ink-soft:#d8d2e6;
  --lilac:#c9a8ee;
  --yes:#5b3bc8;
  --no:#3a1d78;
  --panel:rgba(14,8,22,.82);
  --panel-purple:rgba(110,30,150,.92);
  --info:#e04a55;
  --dot:#8a8596;
}
*{margin:0;padding:0;box-sizing:border-box}
html,body{width:944px;height:1200px;overflow:hidden;background:var(--page)}
body{position:relative;font-family:'Roboto',sans-serif;color:var(--ink)}
.screen{position:absolute;overflow:hidden;border:1px solid var(--frame)}
.backdrop{position:absolute;inset:0;
  background:
   radial-gradient(ellipse 22% 40% at 27% 58%,rgba(255,20,60,.85),transparent 70%),
   radial-gradient(ellipse 30% 55% at 82% 55%,rgba(150,110,160,.45),transparent 70%),
   radial-gradient(ellipse 25% 40% at 20% 25%,rgba(70,40,200,.55),transparent 70%),
   linear-gradient(180deg,#0a0820 0%,#150a24 55%,#050409 100%);}
.backdrop.tall{
  background:
   radial-gradient(ellipse 45% 30% at 80% 40%,rgba(170,120,170,.5),transparent 70%),
   radial-gradient(ellipse 50% 20% at 50% 72%,rgba(190,100,120,.45),transparent 70%),
   radial-gradient(ellipse 20% 30% at 20% 25%,rgba(60,40,190,.5),transparent 70%),
   linear-gradient(180deg,#0b0a1c 0%,#20122c 50%,#0a0610 100%);}
.brand{position:absolute;display:flex;align-items:center;gap:4px;font-family:'Fondamento',cursive;color:var(--lilac);white-space:nowrap}
.brand .mark{border-radius:50%;background:var(--ink)}
.sound{position:absolute;border:1.5px solid var(--ink);border-radius:50%;display:flex;align-items:center;justify-content:center}
.welcome{position:absolute;font-family:'Fondamento',cursive;line-height:1}
.welcome .big{display:block;color:var(--ink)}
.welcome .sub{display:block;color:var(--lilac)}
.age-box{position:absolute;background:var(--panel)}
.age-box h2{font-weight:700;line-height:1.1}
.age-box p{color:var(--ink);line-height:1.35}
.btn{position:absolute;display:flex;align-items:center;justify-content:center;color:var(--ink);font-weight:400}
.btn.yes{background:var(--yes)}
.btn.no{background:var(--no)}
.note{position:absolute;display:flex;color:var(--ink-soft);line-height:1.4}
.note .i{flex:none;border-radius:50%;background:var(--info);color:#fff;display:flex;align-items:center;justify-content:center;font-weight:700}
.links{position:absolute;left:0;right:0;display:flex;justify-content:center;align-items:center;color:var(--ink-soft)}
.links .sep{border-radius:50%;background:var(--dot)}

/* desktop */
.desk{left:47px;top:78px;width:851px;height:604px}
.desk .brand{left:392px;top:22px;font-size:20px}
.desk .brand .mark{width:12px;height:12px}
.desk .sound{left:29px;top:23px;width:30px;height:30px}
.desk .welcome{left:355px;top:148px}
.desk .welcome .big{font-size:42px}
.desk .welcome .sub{font-size:21px;margin-top:2px}
.desk .age-box{left:213px;top:253px;width:424px;height:169px}
.desk .age-box h2{position:absolute;left:36px;top:20px;font-size:19px}
.desk .age-box p{position:absolute;left:36px;top:51px;font-size:9.4px}
.desk .btn{top:77px;height:26px;font-size:10px}
.desk .btn.yes{left:36px;width:136px}
.desk .btn.no{left:198px;width:140px}
.desk .note{left:36px;top:114px;width:370px;font-size:9px;gap:5px}
.desk .note .i{width:11px;height:11px;font-size:8px;margin-top:1px}
.desk .links{top:552px;font-size:10.5px;gap:24px}
.desk .links .sep{width:4px;height:4px}

/* mobile shared */
.mob .brand{font-size:12px}
.mob .brand .mark{width:7px;height:7px}
.mob .links{font-size:6px;gap:6px}
.mob .links .sep{width:2.5px;height:2.5px}

/* mobile dark card */
.m1{width:194px;height:381px}
.m1 .brand{left:19px;top:14px}
.m1 .sound{left:158px;top:16px;width:19px;height:19px}
.m1 .welcome{left:27px;top:94px}
.m1 .welcome .big{font-size:24px}
.m1 .welcome .sub{font-size:12.5px;margin-top:1px}
.m1 .age-box{left:14px;top:159px;width:163px;height:120px}
.m1 .age-box h2{position:absolute;left:22px;top:13px;font-size:11px}
.m1 .age-box p{position:absolute;left:22px;top:34px;width:125px;font-size:5.2px}
.m1 .btn{top:66px;height:16px;font-size:6px}
.m1 .btn.yes{left:22px;width:48px}
.m1 .btn.no{left:79px;width:51px}
.m1 .note{left:22px;top:94px;width:120px;font-size:5px;gap:3px}
.m1 .note .i{width:6px;height:6px;font-size:4.5px}
.m1 .links{top:355px}
.m1a{left:76px;top:762px}
.m1b{left:668px;top:752px}

/* mobile purple card */
.m2{left:370px;top:802px;width:153px;height:294px}
.m2 .brand{left:15px;top:12px;font-size:10px}
.m2 .sound{left:123px;top:11px;width:17px;height:17px}
.m2 .welcome{left:11px;top:56px}
.m2 .welcome .big{font-size:19px}
.m2 .welcome .sub{font-size:10px;margin-top:1px}
.m2 .age-box{left:11px;top:111px;width:133px;height:79px;background:var(--panel-purple)}
.m2 .age-box h2{position:absolute;left:7px;top:11px;font-size:10.5px}
.m2 .age-box p{position:absolute;left:7px;top:29px;width:122px;font-size:5px}
.m2 .btn{top:63px;height:16px;font-size:6px}
.m2 .btn.yes{left:0;width:66px}
.m2 .btn.no{left:66px;width:67px}
.m2 .note{left:7px;top:210px;width:136px;font-size:5px;gap:3px}
.m2 .note .i{width:6px;height:6px;font-size:4.5px}
.m2 .links{top:273px;font-size:6px;gap:5px}
</style>
</head>
<body>

<section class="screen desk">
  <div class="backdrop" role="img" aria-label="Blurred club scene with red neon light and a dancer seated on the right"></div>
  <div class="brand"><span class="mark"></span>Velvet Dare</div>
  <div class="sound"><svg width="14" height="12" viewBox="0 0 14 12"><path d="M1 4h3l4-3v10L4 8H1z" fill="#fff"/><path d="M10 3l2-1M10 6h3M10 9l2 1" stroke="#fff" stroke-width="1.2"/></svg></div>
  <h1 class="welcome"><span class="big">Welcome</span><span class="sub">to Velvet Dare</span></h1>
  <div class="age-box">
    <h2>Are You 18+ Years Old?</h2>
    <p>Please confirm that you are 18 years or older by clicking the "Yes" button below.</p>
    <a class="btn yes">YES</a><a class="btn no">NO</a>
    <div class="note"><span class="i">i</span><span>By clicking "Yes", you acknowledge that you are fully aware of the explicit nature of the content provided in Velvet Dare and are of legal age to access it.</span></div>
  </div>
  <nav class="links"><span>About Us</span><i class="sep"></i><span>FAQ</span><i class="sep"></i><span>Contact Us</span><i class="sep"></i><span>Terms of Service</span><i class="sep"></i><span>Privacy Policy</span></nav>
</section>

<section class="screen mob m1 m1a">
  <div class="backdrop tall" role="img" aria-label="Blurred dancer seated in a dim club"></div>
  <div class="brand"><span class="mark"></span>Velvet Dare</div>
  <div class="sound"><svg width="9" height="8" viewBox="0 0 14 12"><path d="M1 4h3l4-3v10L4 8H1z" fill="#fff"/><path d="M10 3l2-1M10 6h3M10 9l2 1" stroke="#fff" stroke-width="1.2"/></svg></div>
  <h1 class="welcome"><span class="big">Welcome</span><span class="sub">to Velvet Dare</span></h1>
  <div class="age-box">
    <h2>Are You 18+ Years Old?</h2>
    <p>Please confirm that you are 18 years or older by clicking the "Yes" button below.</p>
    <a class="btn yes">YES</a><a class="btn no">NO</a>
    <div class="note"><span class="i">i</span><span>By clicking "Yes", you acknowledge that you are of legal age to access it.</span></div>
  </div>
  <nav class="links"><span>About Us</span><i class="sep"></i><span>FAQ</span><i class="sep"></i><span>Contact Us</span><i class="sep"></i><span>Terms</span></nav>
</section>

<section class="screen mob m2">
  <div class="backdrop tall" role="img" aria-label="Blurred dancer seated in a dim club"></div>
  <div class="brand"><span class="mark"></span>Velvet Dare</div>
  <div class="sound"><svg width="8" height="7" viewBox="0 0 14 12"><path d="M1 4h3l4-3v10L4 8H1z" fill="#fff"/><path d="M10 3l2-1M10 6h3M10 9l2 1" stroke="#fff" stroke-width="1.2"/></svg></div>
  <h1 class="welcome"><span class="big">Welcome</span><span class="sub">to Velvet Dare</span></h1>
  <div class="age-box">
    <h2>Are You 18+ Years Old?</h2>
    <p>Please confirm that you are 18 years or older by clicking the "Yes" button below.</p>
    <a class="btn yes">YES</a><a class="btn no">NO</a>
  </div>
  <div class="note"><span class="i">i</span><span>By clicking "Yes", you acknowledge that you are fully aware of the explicit nature of the content provided in Velvet Dare and are of legal age to access it.</span></div>
  <nav class="links"><span>About Us</span><i class="sep"></i><span>FAQ</span><i class="sep"></i><span>Contact Us</span><i class="sep"></i><span>Terms</span></nav>
</section>

<section class="screen mob m1 m1b">
  <div class="backdrop tall" role="img" aria-label="Blurred dancer seated in a dim club"></div>
  <div class="brand"><span class="mark"></span>Velvet Dare</div>
  <div class="sound"><svg width="9" height="8" viewBox="0 0 14 12"><path d="M1 4h3l4-3v10L4 8H1z" fill="#fff"/><path d="M10 3l2-1M10 6h3M10 9l2 1" stroke="#fff" stroke-width="1.2"/></svg></div>
  <h1 class="welcome"><span class="big">Welcome</span><span class="sub">to Velvet Dare</span></h1>
  <div class="age-box">
    <h2>Are You 18+ Years Old?</h2>
    <p>Please confirm that you are 18 years or older by clicking the "Yes" button below.</p>
    <a class="btn yes">YES</a><a class="btn no">NO</a>
    <div class="note"><span class="i">i</span><span>By clicking "Yes", you acknowledge that you are of legal age to access it.</span></div>
  </div>
  <nav class="links"><span>About Us</span><i class="sep"></i><span>FAQ</span><i class="sep"></i><span>Contact Us</span><i class="sep"></i><span>Terms</span></nav>
</section>

</body>
</html>
```